Can you make a cool and versatile Tarnel Ventures Powerpoint template?
See www.tarnelventures.co.uk and http://www.linkedin.com/company/tarnel-ventures-ltd/ (on the right) to see how the logos are currently used - with interchangeably white and black backgrounds.
Target Market(s)
Marketing managers, product managers in HR technology, HR consultants
Industry/Entity Type
It Company
Font styles to use
Sans Serif
Requirements
Must have
- Master slide design, fonts, color theme, etc. Ideally two variations - one with white background (using colorful logo), one with a darker background (using black/white logo).

```html
<!DOCTYPE html>
<html lang="en">
<head>
<meta charset="utf-8">
<title>Tarnel Ventures – Slide Master (Dark)</title>
<link rel="stylesheet" href="https://fonts.googleapis.com/css2?family=Graduate&family=Cinzel:wght@400&family=Open+Sans:wght@400;600&display=swap">
<style>
  :root {
    --page: #ffffff;
    --slide: #050505;
    --slide-glow: #2e2e2e;
    --accent: #25a9e0;
    --ink: #0a0a0a;
    --white: #ffffff;
    --rule: #3a3a3a;
  }
  html, body {
    margin: 0;
    padding: 0;
    width: 1200px;
    height: 900px;
    overflow: hidden;
    background: var(--page);
  }
  .canvas {
    position: relative;
    width: 1200px;
    height: 900px;
  }
  .slide {
    position: absolute;
    left: 29px;
    top: 179px;
    width: 1132px;
    height: 636px;
    background:
      radial-gradient(ellipse 55% 60% at 50% 35%, var(--slide-glow) 0%, #161616 45%, var(--slide) 85%);
    overflow: hidden;
  }
  .slide-header {
    position: absolute;
    left: 0;
    top: 0;
    width: 1132px;
    height: 120px;
  }
  .bullet-list {
    position: absolute;
    left: 105px;
    top: 92px;
    margin: 0;
    padding: 0;
    list-style: none;
  }
  .main-bullet {
    display: flex;
    align-items: center;
    gap: 14px;
    font-family: "Graduate", serif;
    font-size: 42px;
    color: var(--accent);
    letter-spacing: 1px;
    height: 54px;
  }
  .sub-bullets {
    list-style: none;
    margin: 14px 0 0 88px;
    padding: 0;
  }
  .sub-bullet {
    display: flex;
    align-items: center;
    gap: 10px;
    font-family: "Cinzel", serif;
    font-size: 23px;
    color: var(--white);
    height: 56px;
  }
  .title-band {
    position: absolute;
    left: 16px;
    top: 484px;
    width: 1101px;
    height: 141px;
  }
  .title-band-fill {
    position: absolute;
    inset: 0;
    background: var(--accent);
  }
  .slide-title {
    position: absolute;
    left: 23px;
    top: 14px;
    margin: 0;
    font-family: "Graduate", serif;
    font-weight: 400;
    font-size: 68px;
    line-height: 78px;
    color: var(--ink);
    letter-spacing: 1px;
  }
  .title-rule {
    position: absolute;
    left: 23px;
    top: 87px;
    width: 413px;
    height: 3px;
    background: var(--white);
  }
  .subtitle {
    position: absolute;
    right: 663px;
    top: 100px;
    font-family: "Open Sans", sans-serif;
    font-size: 17px;
    color: var(--white);
  }
  .contact {
    position: absolute;
    right: 170px;
    top: 58px;
    text-align: right;
    font-family: "Open Sans", sans-serif;
    font-size: 10.5px;
    line-height: 17px;
    color: var(--white);
  }
  .brand-box {
    position: absolute;
    left: 946px;
    top: 10px;
    width: 145px;
    height: 121px;
    background: var(--slide);
    display: flex;
    align-items: center;
    justify-content: center;
    text-align: center;
    font-family: "Open Sans", sans-serif;
    font-weight: 600;
    font-size: 17px;
    line-height: 22px;
    color: var(--white);
  }
</style>
</head>
<body>
<main class="canvas">
  <section class="slide">
    <svg class="slide-header" viewBox="0 0 1132 120" aria-hidden="true">
      <line x1="62" y1="47" x2="1035" y2="47" stroke="var(--rule)" stroke-width="4"/>
      <rect x="24" y="32" width="30" height="30" rx="4" transform="rotate(45 39 47)" fill="#111" stroke="#3c3c3c" stroke-width="3"/>
      <circle cx="39" cy="47" r="8" fill="var(--accent)"/>
      <polygon points="1017,13 1117,13 1117,113" fill="var(--accent)"/>
    </svg>

    <ul class="bullet-list">
      <li>
        <div class="main-bullet">
          <svg width="44" height="44" viewBox="0 0 44 44" aria-hidden="true">
            <polygon points="22,4 38,13 38,31 22,40 6,31 6,13" transform="rotate(15 22 22)" fill="none" stroke="var(--accent)" stroke-width="5"/>
          </svg>
          MAIN BULLET
        </div>
        <ul class="sub-bullets">
          <li class="sub-bullet">
            <svg width="34" height="34" viewBox="0 0 34 34" aria-hidden="true">
              <polygon points="17,1 31,9 31,25 17,33 3,25 3,9" transform="rotate(15 17 17)" fill="var(--white)"/>
              <polygon points="17,7 26,12 26,22 17,27 8,22 8,12" transform="rotate(15 17 17)" fill="var(--accent)"/>
            </svg>
            SUB BULLET FORM
          </li>
          <li class="sub-bullet">
            <svg width="34" height="34" viewBox="0 0 34 34" aria-hidden="true">
              <polygon points="17,1 31,9 31,25 17,33 3,25 3,9" transform="rotate(15 17 17)" fill="var(--white)"/>
              <polygon points="17,7 26,12 26,22 17,27 8,22 8,12" transform="rotate(15 17 17)" fill="var(--accent)"/>
            </svg>
            SUB BULLET FORM
          </li>
          <li class="sub-bullet">
            <svg width="34" height="34" viewBox="0 0 34 34" aria-hidden="true">
              <polygon points="17,1 31,9 31,25 17,33 3,25 3,9" transform="rotate(15 17 17)" fill="var(--white)"/>
              <polygon points="17,7 26,12 26,22 17,27 8,22 8,12" transform="rotate(15 17 17)" fill="var(--accent)"/>
            </svg>
            SUB BULLET FORM
          </li>
        </ul>
      </li>
    </ul>

    <footer class="title-band">
      <div class="title-band-fill"></div>
      <h1 class="slide-title">SLIDE TITLE</h1>
      <div class="title-rule"></div>
      <div class="subtitle">BULLET FORM</div>
      <div class="contact">WWW.COMPANYSITE.COM<br>COMPANY@COMPANY.COM</div>
      <div class="brand-box">Tarnel<br>Ventures</div>
    </footer>
  </section>
</main>
</body>
</html>
```